'Tarovin' a financial/crypto-currency exchange in the middle east

On the card we need 1) Name 2) title 3) email address 4) phone number using the same colors and theme as the logo. On one side we just want the logo and we want the whole card to be in blue (same blue as logo) with the logo in the back being white.
Industry/Entity Type
Financial

```html
<!DOCTYPE html>
<html lang="en">
<head>
<meta charset="UTF-8">
<title>Tarovin Business Card</title>
<link href="https://fonts.googleapis.com/css2?family=Rubik:wght@400;500&display=swap" rel="stylesheet">
<style>
  :root {
    --brand-blue: #0b91cd;
    --band-blue: #5aa8dc;
    --white: #ffffff;
    --backdrop: #d4d4d4;
  }
  * { margin: 0; padding: 0; box-sizing: border-box; }
  html, body {
    width: 1200px;
    height: 1000px;
    overflow: hidden;
  }
  body {
    background: var(--backdrop);
    font-family: "Rubik", sans-serif;
    color: var(--white);
    position: relative;
  }
  .card {
    position: absolute;
    background: var(--brand-blue);
  }
  .card-front { left: 170px; top: 112px; width: 590px; height: 338px; }
  .card-back  { left: 390px; top: 558px; width: 600px; height: 342px; }
  .card-frame {
    position: absolute;
    inset: 30px;
    border: 2px solid var(--white);
  }
  .brand {
    position: absolute;
    display: flex;
    align-items: center;
  }
  .brand-mark {
    border: 3px solid var(--white);
    border-radius: 50%;
    flex: none;
  }
  .brand-name {
    font-weight: 500;
    line-height: 1;
    color: var(--white);
  }
  .card-front .brand { left: 144px; top: 122px; gap: 16px; }
  .card-front .brand-mark { width: 90px; height: 90px; }
  .card-front .brand-name { font-size: 50px; }

  .card-back .brand { left: 202px; top: 55px; gap: 10px; }
  .card-back .brand-mark { width: 58px; height: 58px; border-width: 2px; }
  .card-back .brand-name { font-size: 32px; }

  .person-name {
    position: absolute;
    left: 53px;
    top: 132px;
    font-size: 28px;
    font-weight: 400;
    letter-spacing: 1.6px;
    line-height: 1;
  }
  .title-band {
    position: absolute;
    left: 32px;
    top: 170px;
    width: 285px;
    height: 26px;
  }
  .title-band svg { position: absolute; inset: 0; }
  .person-title {
    position: absolute;
    left: 21px;
    top: 3px;
    font-size: 18px;
    letter-spacing: 1.2px;
    line-height: 20px;
  }
  .contact-list {
    position: absolute;
    left: 175px;
    top: 222px;
    list-style: none;
  }
  .contact-item {
    display: flex;
    align-items: center;
    gap: 16px;
    height: 37px;
    font-size: 21px;
    letter-spacing: 1.6px;
  }
  .contact-icon { width: 24px; height: 24px; flex: none; }
</style>
</head>
<body>
  <section class="card card-front" aria-label="Card front">
    <div class="card-frame"></div>
    <div class="brand">
      <span class="brand-mark"></span>
      <span class="brand-name">Tarovin</span>
    </div>
  </section>

  <section class="card card-back" aria-label="Card back">
    <div class="card-frame"></div>
    <div class="brand">
      <span class="brand-mark"></span>
      <span class="brand-name">Tarovin</span>
    </div>
    <p class="person-name">Name of Person</p>
    <div class="title-band">
      <svg width="285" height="26" viewBox="0 0 285 26">
        <path d="M0 0 H285 Q278 20 268 26 H0 Z" fill="var(--band-blue)"/>
      </svg>
      <span class="person-title">Title of person</span>
    </div>
    <ul class="contact-list">
      <li class="contact-item">
        <svg class="contact-icon" viewBox="0 0 24 24" aria-hidden="true">
          <circle cx="12" cy="12" r="10.5" fill="none" stroke="#fff" stroke-width="2"/>
          <path d="M8.2 6.5l2 2.3-1.1 1.4c.8 1.7 2 2.9 3.7 3.7l1.4-1.1 2.3 2-1.3 1.7c-3.9-.5-7.1-3.7-7.6-7.6z" fill="#fff"/>
        </svg>
        <span>Phone number</span>
      </li>
      <li class="contact-item">
        <svg class="contact-icon" viewBox="0 0 24 24" aria-hidden="true">
          <circle cx="12" cy="12" r="11" fill="#fff"/>
          <rect x="6" y="8" width="12" height="8.5" rx="1" fill="var(--brand-blue)"/>
          <path d="M6.5 8.7L12 13l5.5-4.3" fill="none" stroke="#fff" stroke-width="1.3"/>
        </svg>
        <span>name@email.com</span>
      </li>
    </ul>
  </section>
</body>
</html>
```